PowerPoint Design Project

Have a Power Point we want someone to make really cool! About 10 pages and just need someone to build on what we've done.

Target Market(s)

Technology Mfgs/VARs Sales People and VP of Sales

Industry/Entity Type

Build

```html
<!DOCTYPE html>
<html lang="en">
<head>
<meta charset="utf-8">
<title>Make Financing Part of Your Sales Cycle</title>
<link rel="stylesheet" href="https://fonts.googleapis.com/css2?family=Arimo:wght@400;700&family=Open+Sans:wght@600&family=Roboto+Condensed:wght@700&display=swap">
<style>
  :root {
    --brand-blue: #14599b;
    --band-blue: #0d5495;
    --brand-green: #5b8a1f;
    --body-gray: #5a5a5a;
    --page-white: #ffffff;
    --texture-gray: #eceeef;
  }
  * { margin: 0; padding: 0; box-sizing: border-box; }
  html, body { width: 1200px; height: 900px; overflow: hidden; background: var(--page-white); }
  .slide { position: relative; width: 1200px; height: 900px; overflow: hidden; background: var(--page-white); }
  .slide-texture {
    position: absolute; top: 0; right: 0; width: 820px; height: 810px;
    background: radial-gradient(ellipse at 95% 20%, var(--texture-gray) 0%, rgba(236,238,239,0.55) 35%, rgba(255,255,255,0) 70%);
  }
  .brand-lockup {
    position: absolute; left: 70px; top: 321px; width: 465px; height: 117px;
    display: flex; align-items: center; gap: 22px;
  }
  .brand-square { width: 96px; height: 96px; background: var(--brand-blue); flex: none; }
  .brand-name {
    font-family: "Arimo", Arial, sans-serif; font-weight: 700; font-size: 38px;
    line-height: 1.1; color: var(--brand-blue);
  }
  .title {
    position: absolute; right: 60px; top: 312px; text-align: right;
    font-family: "Arimo", Arial, sans-serif; font-weight: 400; font-size: 46px;
    line-height: 66px; color: var(--brand-blue);
  }
  .summary {
    position: absolute; right: 63px; top: 492px; width: 560px; text-align: right;
    font-family: "Open Sans", Arial, sans-serif; font-weight: 600; font-size: 25px;
    line-height: 42px; color: var(--body-gray);
  }
  .footer-rule { position: absolute; left: 0; top: 802px; width: 1200px; height: 8px; background: var(--brand-green); }
  .footer-band { position: absolute; left: 0; top: 810px; width: 1200px; height: 90px; background: var(--band-blue); }
  .footer-copy {
    position: absolute; left: 60px; top: 810px; height: 90px; display: flex; align-items: center;
    font-family: "Roboto Condensed", Arial, sans-serif; font-weight: 700; font-size: 25px;
    color: var(--page-white); letter-spacing: 0.3px;
  }
  .footer-square { position: absolute; left: 1113px; top: 810px; width: 87px; height: 90px; background: var(--page-white); opacity: 0.18; }
</style>
</head>
<body>
  <main class="slide">
    <div class="slide-texture" role="img" aria-label="Soft halftone dot texture fading across the upper right background"></div>

    <div class="brand-lockup">
      <div class="brand-square"></div>
      <div class="brand-name">Harbor Lane Finance</div>
    </div>

    <h1 class="title">Make Financing<br>Part of Your Sales Cycle</h1>

    <p class="summary">Lorem ipsum dolor sit ipsum Lorem ipsum dolor sit ipsum Lorem ipsum dolor sit ipsum Lorem ipsum</p>

    <div class="footer-rule"></div>
    <footer class="footer-band"></footer>
    <div class="footer-copy">Copyright@Harbor Lane Finance</div>
    <div class="footer-square"></div>
  </main>
</body>
</html>
```